Lose Up To 1 LB Of Fat Per Day

We need a double sided street sign for our weight loss clinic. We need the doctors picture to the right side of the sign and we need a challenge “Lose Up To 1 Pound Of Fat Per Day” included in the signage.
Our color scheme for the clinic are black, white, teal and silver.
The phone number should be at the bottom of the sign
555-206–3948

Target Market(s)

Weight Loss

Font styles to use
Sans Serif

```html
<!DOCTYPE html>
<html lang="en">
<head>
<meta charset="utf-8">
<title>Boundless Wellness Centers – Street Sign</title>
<link href="https://fonts.googleapis.com/css2?family=Josefin+Sans:wght@400;600;700&family=Montserrat:wght@800;900&family=Oswald:wght@500&family=Nunito:wght@800&display=swap" rel="stylesheet">
<style>
  :root {
    --teal: #14988f;
    --teal-light: #5cc6c0;
    --teal-pale: #d5efee;
    --ink: #111111;
    --white: #ffffff;
    --silver: #cfd3d4;
    --page: #e4e6e7;
  }
  * { margin: 0; padding: 0; box-sizing: border-box; }
  html, body { width: 841px; height: 1200px; overflow: hidden; background: var(--page); }
  .sign {
    position: absolute; left: 20px; top: 338px;
    width: 801px; height: 523px; overflow: hidden;
    background: linear-gradient(100deg, var(--white) 45%, #eaf6f6 100%);
    box-shadow: 0 10px 24px rgba(0,0,0,.25);
  }
  .sign__waves { position: absolute; inset: 0; }
  .brand {
    position: absolute; left: 150px; top: 48px;
    font-family: "Josefin Sans", sans-serif; font-weight: 600; color: var(--ink);
    display: flex; align-items: center; gap: 12px; white-space: nowrap;
  }
  .brand__dot { width: 22px; height: 22px; border-radius: 50%; background: var(--ink); }
  .brand__name { line-height: 1; }
  .brand__name span { display: block; }
  .brand__name .l1 { font-size: 27px; letter-spacing: .5px; }
  .brand__name .l2 { font-size: 16px; margin-top: 4px; }
  .offer-intro {
    position: absolute; left: 47px; top: 142px; width: 330px;
    display: flex; align-items: center; justify-content: center; gap: 10px;
    font-family: "Josefin Sans", sans-serif; font-size: 36px; color: var(--ink);
    white-space: nowrap;
  }
  .offer-intro .rule { width: 42px; height: 2px; background: var(--ink); }
  .offer-intro b { color: var(--teal); font-weight: 700; }
  .offer-amount {
    position: absolute; left: 30px; top: 182px; width: 375px; text-align: center;
    font-family: "Oswald", sans-serif; font-weight: 500; font-size: 122px; line-height: 1;
    color: var(--teal); white-space: nowrap;
  }
  .offer-tail {
    position: absolute; left: 40px; top: 300px; width: 370px; text-align: center;
    font-family: "Montserrat", sans-serif; font-weight: 900; font-size: 40px; line-height: 1.2;
    color: var(--ink); white-space: nowrap;
  }
  .offer-tail em { font-style: normal; color: var(--teal); }
  .phone {
    position: absolute; left: 37px; top: 366px; width: 367px; height: 57px;
    background: var(--ink); border-radius: 29px;
    display: flex; align-items: center; gap: 12px; padding-left: 10px;
  }
  .phone__icon { width: 42px; height: 42px; flex: none; }
  .phone__number {
    font-family: "Montserrat", sans-serif; font-weight: 800; font-size: 36px;
    color: var(--white); white-space: nowrap;
  }
  .doctor-tag {
    position: absolute; left: 490px; top: 45px; width: 263px; height: 40px;
    background: var(--teal); border: 2px solid var(--white); border-radius: 20px;
    font-family: "Nunito", sans-serif; font-weight: 800; font-size: 25px; color: var(--white);
    display: flex; align-items: center; justify-content: center; white-space: nowrap;
  }
  .doctor-tag::after {
    content: ""; position: absolute; left: 50%; bottom: -16px; transform: translateX(-50%);
    border-left: 11px solid transparent; border-right: 11px solid transparent;
    border-top: 14px solid var(--teal);
  }
  .doctor-photo {
    position: absolute; left: 482px; top: 119px; width: 296px; height: 404px;
    border-radius: 90px 90px 0 0;
    background: linear-gradient(180deg, #c9b6a6 0%, #a89384 28%, #2a2a2e 40%, #111 100%);
  }
</style>
</head>
<body>
  <section class="sign">
    <svg class="sign__waves" viewBox="0 0 801 523" aria-hidden="true">
      <path d="M520 523 C660 470 740 400 801 260 L801 523 Z" fill="var(--teal-light)"/>
      <path d="M600 523 C700 470 770 410 801 340 L801 523 Z" fill="var(--teal)"/>
      <path d="M0 410 C200 450 450 455 801 405 L801 523 L0 523 Z" fill="var(--teal-pale)"/>
      <path d="M0 445 C220 470 450 470 801 425 L801 523 L0 523 Z" fill="var(--teal-light)"/>
      <path d="M0 470 C240 500 480 490 801 450 L801 523 L0 523 Z" fill="var(--white)"/>
      <path d="M0 482 C250 510 500 505 801 470 L801 523 L0 523 Z" fill="var(--teal)"/>
    </svg>

    <div class="brand">
      <span class="brand__dot"></span>
      <div class="brand__name"><span class="l1">BOUNDLESS</span><span class="l2">WELLNESS CENTERS</span></div>
    </div>

    <div class="offer-intro"><span class="rule"></span><span><b>LOSE</b> UP TO</span><span class="rule"></span></div>
    <div class="offer-amount">1 POUND</div>
    <div class="offer-tail">OF <em>FAT</em> PER DAY</div>

    <div class="phone">
      <svg class="phone__icon" viewBox="0 0 42 42" aria-hidden="true">
        <circle cx="21" cy="21" r="19" fill="var(--white)" stroke="var(--teal)" stroke-width="4"/>
        <path d="M14 13 l4 -1 l2 5 l-2.5 2 a12 12 0 0 0 6 6 l2 -2.5 l5 2 l-1 4 c-9 1 -17 -7 -15.5 -15.5 z" fill="var(--ink)"/>
      </svg>
      <span class="phone__number">555-206–3948</span>
    </div>

    <div class="doctor-tag">Dr. Martin Kessler</div>
    <div class="doctor-photo" role="img" aria-label="Portrait photo of the clinic doctor in a dark suit and purple tie, hands clasped"></div>
  </section>
</body>
</html>
```